Corporate Financing/Banking Website Design

I need a website for a corporate financing website.

The company helps other companies raise money for financing.

Content for the website can be found here: https://www.pinemoor.ca/northbaycapital/

Each section from the content in the main page above should have a corresponding image associated with each "Section"

1. Financing solutions that will be provided by Tarnwell Ridge Capital will include:

2. The financing solutions mentioned above will assist businesses to:

3. The industry sectors focussed on are, but not limited to:

We need to make sure that the website has clear buttons for the visitor to "Apply Now" and "Book an Appointment" to apply for financing options.

We need the following pages designed
Home
About Us
Financing Solutions
Contact Us.

For the Logo:

The company name is Tarnwell Ridge Capital. Something that emphasizes direction and progress and is related to Corporate finance

Something professional that conveys confidence

Target Market(s)

Corporation and large business

Logo Text

Tarnwell Ridge Capital

Number of Pages Required

4 page

Colors
0393ce

Requirements
Must have
• Use the color: #OA64BC

Please ensure 'Apply Now' & 'Book an Appointment' buttons are very clear and placed appropriately on the webpage.

In the Footer I would like 'T&C's' and 'Privacy Policy' links

Social Media icon links will be 'LinkedIn / Facebook/ Twitter and we should keep these in Footer and Contacts page section.
Should not have
• - Do not include a search field

```html
<!DOCTYPE html>
<html lang="en">
<head>
<meta charset="utf-8">
<title>Tarnwell Ridge Capital</title>
<link rel="stylesheet" href="https://fonts.googleapis.com/css2?family=Quicksand:wght@500;600;700&family=Lato:wght@400;700&display=swap">
<style>
:root{
  --blue:#0a8ad0;
  --blue-deep:#0a64bc;
  --blue-band:#0f8bcc;
  --blue-light:#1e9fdc;
  --ink:#1d1d1f;
  --body:#4a4a4a;
  --line:#cfd3d8;
  --white:#ffffff;
}
*{box-sizing:border-box;margin:0;padding:0}
html,body{width:1200px;height:3866px;overflow:hidden;background:var(--white)}
body{position:relative;font-family:"Lato",sans-serif;color:var(--ink)}
.abs{position:absolute}
.heading{font-family:"Quicksand",sans-serif;font-weight:600}
.btn{position:absolute;background:var(--blue-deep);color:var(--white);font-size:12px;display:flex;align-items:center;justify-content:center;border-radius:3px;text-decoration:none}

/* header */
.site-header{left:0;top:0;width:1200px;height:78px;background:var(--white)}
.brand{left:147px;top:18px;display:flex;align-items:center;gap:10px}
.brand-dot{width:30px;height:30px;border-radius:50%;background:var(--blue)}
.brand-name{font-family:"Quicksand",sans-serif;font-weight:600;font-size:22px;color:var(--blue)}
.main-nav{left:525px;top:26px;display:flex;gap:36px;font-size:12px;color:var(--ink)}
.header-btn{left:906px;top:18px;width:141px;height:34px}

/* hero */
.hero-photo{left:0;top:78px;width:1200px;height:675px;background:linear-gradient(110deg,#1d2228 0%,#3b4651 45%,#6d7d8c 75%,#c9ccd0 100%)}
.hero-title{left:148px;top:318px;font-size:44px;line-height:46px;color:var(--white);font-weight:600}
.hero-btn{left:148px;top:493px;width:141px;height:37px}

/* about */
.about{left:0;top:753px;width:1200px;height:695px;background:linear-gradient(180deg,#ffffff 0%,#f4f8fc 60%,#ffffff 100%)}
.about-title{left:640px;top:942px;font-size:28px;color:var(--ink);font-weight:500}
.about-text{left:646px;top:1010px;width:410px;font-size:11px;line-height:22.5px;color:var(--body)}
.about-text p+p{margin-top:22px}
.about-btn{left:646px;top:1248px;width:101px;height:29px}

/* solutions band */
.solutions{left:0;top:1448px;width:1200px;height:1085px;background:linear-gradient(135deg,#0b78bd 0%,var(--blue-band) 45%,var(--blue-light) 100%)}
.solutions-title{left:0;top:1518px;width:1200px;text-align:center;font-size:30px;color:var(--white);font-weight:500}
.solutions-sub{left:395px;top:1564px;width:402px;text-align:center;font-size:11px;color:var(--white);padding-bottom:8px;border-bottom:1px solid rgba(255,255,255,.8)}
.solutions-note{left:0;top:1601px;width:1200px;text-align:center;font-size:11px;color:var(--white)}
.tiles{left:150px;top:1662px;width:897px;height:372px;display:flex}
.tile{position:relative;flex:1;height:100%}
.tile-label{position:absolute;left:0;right:0;bottom:20px;text-align:center;font-size:20px;color:var(--white);font-weight:600}
.tile-1{background:linear-gradient(160deg,#dfe7ee 0%,#b3c3d3 50%,#4c5d6e 100%)}
.tile-2{background:linear-gradient(160deg,#2e3236 0%,#7f8790 45%,#e4e7ea 70%,#5d646b 100%)}
.tile-3{background:linear-gradient(160deg,#f5f5f5 0%,#d8d9db 55%,#2b2e31 100%)}
.solutions-foot{left:0;top:2063px;width:1200px;text-align:center;font-size:11px;color:var(--white)}

.assist-title{left:120px;top:2182px;font-size:28px;line-height:46px;color:var(--white);font-weight:500;letter-spacing:.3px}
.assist-list{left:124px;top:2303px;list-style:none;font-size:11px;color:var(--white)}
.assist-list li{height:33px;display:flex;align-items:center;gap:14px}
.assist-list svg{flex:none}
.assist-photo{left:597px;top:2175px;width:603px;height:428px;background:linear-gradient(150deg,#3a3f44 0%,#7f868c 35%,#e6e8ea 60%,#b8bec4 100%)}

/* sectors */
.sectors-title{left:0;top:2641px;width:1200px;text-align:center;font-size:29px;color:var(--ink);font-weight:500}
.sectors-map{left:0;top:2700px}
.sector-label{font-family:"Lato",sans-serif;font-size:17px;fill:#333}

/* footer */
.site-footer{left:0;top:3468px;width:1200px;height:339px;background:var(--blue)}
.footer-brand{left:150px;top:3575px;display:flex;align-items:center;gap:14px}
.footer-brand .brand-dot{width:50px;height:50px;background:var(--white)}
.footer-brand .brand-name{font-size:36px;color:var(--white)}
.social{left:165px;top:3667px;display:flex;gap:19px}
.social span{width:30px;height:30px;border-radius:50%;background:var(--white)}
.footer-col-title{font-size:20px;color:var(--white);font-weight:500}
.quick-links{left:596px;top:3594px;list-style:none;font-size:11px;color:var(--white)}
.quick-links li{height:31.5px}
.contact-list{left:834px;top:3594px;list-style:none;font-size:11px;color:var(--white)}
.contact-list li{display:flex;gap:12px;min-height:31.5px}
.contact-list li div{line-height:31.5px;margin-top:-10px}
.contact-list svg{flex:none;margin-top:1px}
.legal{left:0;top:3807px;width:1200px;height:59px;background:var(--white);font-size:11px;color:#555}
.legal-copy{left:148px;top:24px}
.legal-links{left:826px;top:24px;display:flex;gap:18px}
</style>
</head>
<body>

<header class="abs site-header">
  <div class="abs brand"><span class="brand-dot"></span><span class="brand-name">Tarnwell Ridge Capital</span></div>
  <nav class="abs main-nav"><span>Home</span><span>About Us</span><span>Financing Solutions</span><span>Contact Us</span></nav>
  <a class="btn header-btn">Book an appointment</a>
</header>

<div class="abs hero-photo" role="img" aria-label="Two businessmen reviewing documents at a laptop in an office"></div>
<h1 class="abs heading hero-title">We provide the best<br>financial solutions for<br>your Business</h1>
<a class="btn hero-btn">Book an appointment</a>

<section class="abs about"></section>
<svg class="abs" style="left:100px;top:890px" width="500" height="460" viewBox="0 0 500 460" aria-hidden="true">
  <circle cx="240" cy="229" r="222" fill="var(--blue)"/>
</svg>
<div class="abs" style="left:144px;top:899px;width:441px;height:441px;border-radius:50%;background:linear-gradient(135deg,#e8e3dc 0%,#b08a62 45%,#f2f0ec 100%)" role="img" aria-label="Business colleagues smiling during a meeting at a table"></div>
<h2 class="abs heading about-title">About Tarnwell Ridge Capital</h2>
<div class="abs about-text">
  <p>Tarnwell Ridge Capital was created by its founder and CEO, Halden Mercer, for the purpose of meeting the continued growing requirements of businesses for working capital solutions in the frame of operational efficiency, business growth and credit risk mitigation needs.</p>
  <p>Tarnwell Ridge Capital brings global, regional and local experience in trade finance, supply chain finance and commodity finance to the marketplace and will be best placed to structure, tailor and provide a financing solution for your business.</p>
</div>
<a class="btn about-btn">Read More</a>

<section class="abs solutions"></section>
<h2 class="abs heading solutions-title">Financial Solutions</h2>
<p class="abs solutions-sub">Financing solutions that will be provided by Tarnwell Ridge Capital will include:</p>
<p class="abs solutions-note">Receivables Finance, which includes:</p>
<div class="abs tiles">
  <div class="tile tile-1" role="img" aria-label="Calculator, banknotes and financial charts on a desk"><span class="tile-label heading">Receivables Financing</span></div>
  <div class="tile tile-2" role="img" aria-label="Online banking page on a computer screen beside a laptop"><span class="tile-label heading">Factoring</span></div>
  <div class="tile tile-3" role="img" aria-label="Stack of printed invoice documents"><span class="tile-label heading">Invoice Financing</span></div>
</div>
<p class="abs solutions-foot">With structured optionsof; disclosed, confidential, single debtor, single invoice, multi debtor or total pool purchase financing available.</p>

<h2 class="abs heading assist-title">The financing solutions mentioned<br>above will assist businesses</h2>
<ul class="abs assist-list">
  <li><svg width="14" height="14" viewBox="0 0 14 14"><circle cx="7" cy="7" r="5.5" fill="none" stroke="#fff" stroke-width="1.3"/><path d="M4.3 7.2l1.9 1.9 3.5-3.8" fill="none" stroke="#fff" stroke-width="1.3"/></svg>Monetise its receivables to accelerate its cash cycle</li>
  <li><svg width="14" height="14" viewBox="0 0 14 14"><circle cx="7" cy="7" r="5.5" fill="none" stroke="#fff" stroke-width="1.3"/><path d="M4.3 7.2l1.9 1.9 3.5-3.8" fill="none" stroke="#fff" stroke-width="1.3"/></svg>Mitigate debtor credit risk</li>
  <li><svg width="14" height="14" viewBox="0 0 14 14"><circle cx="7" cy="7" r="5.5" fill="none" stroke="#fff" stroke-width="1.3"/><path d="M4.3 7.2l1.9 1.9 3.5-3.8" fill="none" stroke="#fff" stroke-width="1.3"/></svg>Minimise payment risks</li>
  <li><svg width="14" height="14" viewBox="0 0 14 14"><circle cx="7" cy="7" r="5.5" fill="none" stroke="#fff" stroke-width="1.3"/><path d="M4.3 7.2l1.9 1.9 3.5-3.8" fill="none" stroke="#fff" stroke-width="1.3"/></svg>Optimise credit limits so as to boost sales growth</li>
  <li><svg width="14" height="14" viewBox="0 0 14 14"><circle cx="7" cy="7" r="5.5" fill="none" stroke="#fff" stroke-width="1.3"/><path d="M4.3 7.2l1.9 1.9 3.5-3.8" fill="none" stroke="#fff" stroke-width="1.3"/></svg>Use its working capital to fund its business</li>
</ul>
<div class="abs assist-photo" role="img" aria-label="Hands signing paperwork with charts beside a laptop"></div>

<h2 class="abs heading sectors-title">The industry sectors focussed on are, but not limited to:</h2>
<svg class="abs sectors-map" width="1200" height="700" viewBox="0 2700 1200 700" role="img" aria-label="Industry sectors arranged in a circle">
  <circle cx="597" cy="3060" r="228" fill="none" stroke="#c8ccd1" stroke-width="1.5"/>
  <circle cx="597" cy="3060" r="105" fill="var(--blue)"/>
  <g fill="none" stroke="var(--blue-deep)" stroke-width="1.5">
    <path d="M597 2772v28"/>
    <path d="M284 2822h106l30 42"/>
    <path d="M948 2822h-140l-36 42"/>
    <path d="M190 2997h96l42 28"/>
    <path d="M1030 2999h-130l-45 22"/>
    <path d="M215 3239h115l42 -33"/>
    <path d="M996 3239h-168l-23 -14"/>
    <path d="M375 3372h110l20 -45"/>
    <path d="M990 3370h-280l-20 -40"/>
  </g>
  <g class="sector-label" text-anchor="middle">
    <text x="597" y="2763">INFRASTRUCTURE</text>
    <text x="338" y="2813">RESOURCES</text>
    <text x="878" y="2813">CONSTRUCTION</text>
    <text x="218" y="2988">FMCG</text>
    <text x="974" y="2990">CONSULTING</text>
    <text x="269" y="3230">INDUSTRIAL</text>
    <text x="946" y="3230">TELECOMM</text>
    <text x="416" y="3362">SERVICES</text>
    <text x="864" y="3360">INFORMATION TECHNOLOGY</text>
  </g>
  <g fill="var(--blue)">
    <circle cx="597" cy="2835" r="36"/>
    <circle cx="449" cy="2897" r="36"/>
    <circle cx="744" cy="2892" r="36"/>
    <circle cx="368" cy="3036" r="36"/>
    <circle cx="819" cy="3024" r="36"/>
    <circle cx="407" cy="3187" r="36"/>
    <circle cx="795" cy="3187" r="36"/>
    <circle cx="518" cy="3282" r="36"/>
    <circle cx="682" cy="3282" r="36"/>
  </g>
  <g fill="#fff">
    <path d="M583 2847l14-26 14 26z"/>
    <circle cx="449" cy="2897" r="14" fill="none" stroke="#fff" stroke-width="3"/>
    <path d="M730 2906l14-28 14 28z"/>
    <rect x="354" y="3026" width="28" height="20" rx="2"/>
    <rect x="804" y="3012" width="20" height="14" rx="2"/><rect x="816" y="3022" width="18" height="13" rx="2"/>
    <path d="M393 3200v-16l9 6v-6l9 6v-12h8v22z"/>
    <path d="M788 3203l7-28 7 28z"/>
    <circle cx="518" cy="3282" r="9"/><circle cx="518" cy="3282" r="14" fill="none" stroke="#fff" stroke-width="4" stroke-dasharray="5 4"/>
    <circle cx="682" cy="3282" r="13" fill="none" stroke="#fff" stroke-width="3"/><circle cx="682" cy="3282" r="4"/>
  </g>
</svg>

<footer class="abs site-footer"></footer>
<div class="abs footer-brand"><span class="brand-dot"></span><span class="brand-name">Tarnwell Ridge Capital</span></div>
<div class="abs social" aria-label="Social links"><span></span><span></span><span></span></div>
<h3 class="abs heading footer-col-title" style="left:596px;top:3543px">Quick Links</h3>
<ul class="abs quick-links"><li>Home</li><li>About Us</li><li>Financing Solutions</li><li>Contact Us</li></ul>
<h3 class="abs heading footer-col-title" style="left:834px;top:3543px">Contact info..</h3>
<ul class="abs contact-list">
  <li><svg width="13" height="13" viewBox="0 0 13 13"><path d="M3 1l2 3-1.3 1.3a7 7 0 003.9 3.9L9 8l3 2-1.2 2A9 9 0 011 2.2z" fill="#fff"/></svg><div>+00 555 010 2040</div></li>
  <li><svg width="13" height="13" viewBox="0 0 13 13"><rect x="1" y="3" width="11" height="8" fill="#fff"/><path d="M1 3l5.5 4.5L12 3" fill="none" stroke="var(--blue)"/></svg><div>info@tarnwellridge.com</div></li>
  <li><svg width="13" height="15" viewBox="0 0 13 15"><path d="M6.5 14S1.5 8.5 1.5 5.5a5 5 0 0110 0C11.5 8.5 6.5 14 6.5 14z" fill="#fff"/><circle cx="6.5" cy="5.5" r="1.8" fill="var(--blue)"/></svg><div>Suite 4, 210 Harbour View Road<br>Kelmont NSW<br>2100, Australia</div></li>
</ul>
<div class="abs legal">
  <span class="abs legal-copy">© 2021 Tarnwell Ridge Capital - All Rights Reserved.</span>
  <span class="abs legal-links"><span>Terms &amp; Conditions</span><span>|</span><span>Privacy Policy</span></span>
</div>

</body>
</html>
```